Display ads - Med spa Velaxin promotion

Please create an ad creative for a promotional special for a med spa:
First-time customers who book a Velaxin appointment receive $50 off the Velaxin treatment

Please have an aspect of diversity in the ad (the company is black and woman-owned, so more than just white people in the ad creative

The company goes for "clean and tranquil" as part of their aesthetic

Attached here are the logo and picture of the homepage, and other images on the website, typical of the aesthetic of the company identity

you can find the website here for inspiration: thepetalroomspa.com

Please no "black and white" photography, full color only, thank you!

Target Market(s)

New Haven, Connecticut, wealthy individuals who want to look and feel younger, want great skin, and want to feel youthful

Industry/Entity Type

Medspa/beauty

Requirements
Must have
• Need 5 sizes that fit the following Medium rectangle: 300×250; Large rectangle: 300×600 ; 728x90, 300x50; 160x600
Nice to have
• Clean, refined, bright
Should not have
• black and white photos, cartoonish, or drawn items

```html
<!DOCTYPE html>
<html lang="en">
<head>
<meta charset="UTF-8">
<title>The Petal Room Spa – Velaxin Offer 300×250</title>
<link rel="stylesheet" href="https://fonts.googleapis.com/css2?family=Raleway:wght@500&family=Montserrat:wght@500&display=swap">
<style>
  :root {
    --page: #eef2f1;
    --marble-light: #f6f6f6;
    --marble-mid: #ebebeb;
    --navy: #0f2d5c;
    --cyan: #00b9e3;
    --mint: #55d39a;
    --mint-soft: #9fe5c0;
    --leaf: #cfe9ea;
    --photo-skin: #c98e6a;
    --photo-hair: #5a3a24;
    --photo-light: #f3ece6;
  }
  * { margin: 0; padding: 0; box-sizing: border-box; }
  html, body {
    width: 1200px;
    height: 1200px;
    overflow: hidden;
    background: var(--page);
  }
  .ad {
    position: absolute;
    left: 0;
    top: 100px;
    width: 1200px;
    height: 1000px;
    overflow: hidden;
    background: linear-gradient(160deg, var(--marble-light) 0%, var(--marble-mid) 50%, var(--marble-light) 100%);
  }
  .leaf-spray {
    position: absolute;
    border-radius: 50%;
    background: radial-gradient(ellipse at center, var(--leaf) 0%, rgba(207,233,234,0) 70%);
    opacity: .8;
  }
  .leaf-spray--top { left: 500px; top: -20px; width: 340px; height: 280px; }
  .leaf-spray--bottom { left: -20px; top: 640px; width: 420px; height: 260px; }
  .portrait {
    position: absolute;
    left: 590px;
    top: 60px;
    width: 610px;
    height: 860px;
    border-radius: 48% 0 0 0;
    background:
      radial-gradient(ellipse 30% 26% at 52% 44%, var(--photo-skin) 0%, rgba(201,142,106,0) 100%),
      radial-gradient(ellipse 55% 60% at 55% 40%, var(--photo-hair) 0%, rgba(90,58,36,.85) 55%, rgba(90,58,36,0) 75%),
      radial-gradient(ellipse 60% 30% at 55% 95%, var(--photo-skin) 0%, rgba(201,142,106,0) 100%),
      var(--photo-light);
  }
  .brand {
    position: absolute;
    left: 153px;
    top: 59px;
    display: flex;
    align-items: center;
  }
  .brand__dot {
    width: 110px;
    height: 110px;
    border-radius: 50%;
    border: 5px solid var(--cyan);
  }
  .brand__divider {
    width: 2px;
    height: 144px;
    margin: 0 28px 0 40px;
    background: var(--navy);
  }
  .brand__name {
    font-family: "Montserrat", sans-serif;
    font-weight: 500;
    font-size: 38px;
    line-height: 43px;
    color: var(--navy);
  }
  .brand__tagline {
    position: absolute;
    left: 167px;
    top: 212px;
    font-family: "Montserrat", sans-serif;
    font-weight: 500;
    font-size: 21px;
    letter-spacing: .5px;
    color: var(--navy);
  }
  .offer {
    position: absolute;
    left: 20px;
    top: 300px;
    width: 600px;
    text-align: center;
    font-family: "Raleway", sans-serif;
    font-weight: 500;
    color: var(--navy);
  }
  .offer__lead {
    font-size: 45px;
    line-height: 50px;
    letter-spacing: -.3px;
  }
  .offer__deal {
    width: 522px;
    margin: 22px auto 0;
    padding: 4px 0 6px;
    border-top: 2px solid var(--cyan);
    border-bottom: 2px solid var(--cyan);
    color: var(--cyan);
    font-size: 56px;
    line-height: 64px;
  }
  .offer__deal-small { font-size: 36px; }
  .offer__tail {
    margin-top: 14px;
    font-size: 45px;
    line-height: 52px;
    letter-spacing: -.3px;
  }
  .wave {
    position: absolute;
    left: 0;
    top: 0;
    width: 1200px;
    height: 1000px;
  }
</style>
</head>
<body>
  <main class="ad">
    <div class="leaf-spray leaf-spray--top" role="img" aria-label="Faint watercolour leaf sprig decoration"></div>
    <div class="leaf-spray leaf-spray--bottom" role="img" aria-label="Faint watercolour leaf sprig decoration"></div>

    <div class="portrait" role="img" aria-label="Colour photo of a smiling woman with voluminous curly hair in a white top"></div>

    <div class="brand">
      <span class="brand__dot"></span>
      <span class="brand__divider"></span>
      <span class="brand__name">The Petal<br>Room<br>Spa</span>
    </div>
    <p class="brand__tagline">Your Skin Deserves Better</p>

    <section class="offer">
      <h1 class="offer__lead">FIRST-TIME CUSTOMERS<br>WHO BOOK A<br>VELAXIN APPOINTMENT</h1>
      <p class="offer__deal">RECEIVE $50 <span class="offer__deal-small">OFF</span></p>
      <p class="offer__tail">THE VELAXIN TREATMENT</p>
    </section>

    <svg class="wave" viewBox="0 0 1200 1000" aria-hidden="true">
      <path d="M0 786 C 40 880, 200 925, 420 932 C 620 936, 820 880, 1100 812 L 1100 816 C 820 888, 620 944, 420 942 C 200 938, 40 900, 0 860 Z" fill="var(--mint)"/>
      <path d="M0 875 C 200 930, 450 950, 650 920 C 850 885, 980 810, 1200 802 L 1200 1000 L 0 1000 Z" fill="var(--cyan)"/>
      <path d="M0 786 C 20 840, 80 870, 180 890 L 0 875 Z" fill="var(--mint-soft)"/>
    </svg>
  </main>
</body>
</html>
```